Redesign of our website

we are working on redesign our website. however project only require the main page to be done.

The detail requirement is in word document.

```html
<!DOCTYPE html>
<html lang="en">
<head>
<meta charset="utf-8">
<title>Steady Cart – Home</title>
<link href="https://fonts.googleapis.com/css2?family=Open+Sans:wght@400;600;700&family=Arimo:wght@400;700&display=swap" rel="stylesheet">
<style>
:root{
  --navy:#2e4262;
  --navy-dark:#23344f;
  --page:#ffffff;
  --orange:#f26b1d;
  --orange-dark:#e05a10;
  --red:#e43c1c;
  --green:#1f8a3a;
  --text:#222;
  --muted:#666;
  --line:#d9d9d9;
  --tab:#eeeeee;
}
*{box-sizing:border-box;margin:0;padding:0}
html,body{width:921px;height:1200px;overflow:hidden;background:var(--navy)}
body{font-family:"Open Sans",sans-serif;color:var(--text);font-size:11px}
.stage{width:1002px;height:1306px;transform:scale(.9192);transform-origin:0 0;position:relative;background:var(--navy)}
.abs{position:absolute}
.page{left:15px;top:12px;width:972px;height:1225px;background:var(--page)}
.footer-bar{left:15px;top:1248px;width:972px;height:44px;background:var(--page);font-size:10px;display:flex;align-items:center;padding:0 14px}
a{color:inherit;text-decoration:none}

/* header */
.brand{left:35px;top:40px;font-family:"Arimo",sans-serif;font-weight:700;font-size:30px;color:var(--green);display:flex;align-items:center;gap:8px}
.brand .mark{width:26px;height:26px;background:var(--orange)}
.brand small{position:absolute;left:0;top:40px;font-size:10px;color:var(--muted);font-weight:400}
.cart{left:716px;top:12px;width:218px;height:30px;background:var(--navy);border-radius:0 0 4px 4px;color:#fff;font-size:12px;display:flex;align-items:center;padding:0 10px;gap:10px}
.cart .ico{width:14px;height:10px;background:#8cc63f}
.follow{right:34px;top:87px;font-size:13px;font-weight:600;color:#333;display:flex;gap:12px;align-items:center}
.follow span.sq{display:inline-block;width:14px;height:14px;background:#3b5a99;vertical-align:-2px;margin-left:4px}
.follow span.sq.alt{background:#3aaee8}

/* nav */
.nav{left:32px;top:113px;width:936px;height:39px;background:var(--navy);display:flex;align-items:center;color:#fff;font-size:12px}
.nav .cats{width:178px;padding-left:16px;display:flex;align-items:center;gap:8px}
.nav .cats i{display:inline-block;width:16px;height:16px;border-radius:50%;background:#fff;position:relative}
.nav .cats i:after{content:"";position:absolute;left:4px;top:6px;border:4px solid transparent;border-top-color:var(--navy)}
.nav ul{list-style:none;display:flex}
.nav li{padding:0 14px;border-left:1px solid #55688a}
.nav li:first-child{border:0;color:var(--orange)}
.nav .live{background:var(--orange);padding:0 2px}
.subnav{left:210px;top:152px;width:758px;height:34px;background:var(--orange);color:#fff;font-size:12px;display:flex;align-items:center;padding:0 14px}
.subnav a{padding:0 12px;border-left:1px solid #ffb58a}
.subnav a:first-child{border:0;padding-left:0}
.subnav .search{margin-left:auto;display:flex;align-items:center;gap:8px}
.subnav input{width:170px;height:18px;border:1px solid #ccc}
.btn-go{background:#333;color:#fff;font-size:11px;padding:2px 6px;border:1px solid #fff}

/* left sidebar */
.box{border:1px solid var(--line);background:#fff}
.cat-list{left:32px;top:162px;width:166px;height:290px;padding:8px 12px;list-style:none}
.cat-list li{font-size:10px;padding:4px 0 4px 16px;border-bottom:1px dotted #bbb;position:relative}
.cat-list li:before{content:"";position:absolute;left:2px;top:7px;width:6px;height:6px;border:1px dotted #333}
.side-head{background:var(--navy);color:#fff;font-family:"Arimo",sans-serif;font-size:14px;padding:7px 9px}
.side-head.orange{background:var(--orange)}
.subscribe{left:32px;top:463px;width:166px;height:138px}
.subscribe .row{display:flex;gap:6px;padding:10px 8px 6px}
.subscribe .field{width:114px;height:20px;border:1px solid #ccc;font-size:9px;color:#999;padding:3px 6px}
.subscribe .social{display:flex;justify-content:space-between;align-items:center;padding:5px 8px;font-size:12px}
.chip{color:#fff;font-weight:700;font-size:11px;padding:2px 5px}
.chip.b{background:#3b5a99}.chip.t{background:#3aaee8}
.topdeal{left:32px;top:614px;width:166px;height:298px}
.deal{display:flex;gap:8px;padding:9px 6px 0}
.thumb{width:65px;height:65px;border:1px solid var(--line);background:linear-gradient(#3a3a3a,#111);flex:none}
.deal p{font-size:11px}
.price{color:var(--red);font-weight:700;font-size:11px;margin-top:16px}

/* banner */
.banner{left:210px;top:202px;width:562px;height:204px;background:linear-gradient(90deg,#f5e2c8 0%,#e9a46a 38%,#1b6a34 45%,#2a7a3c 100%);overflow:hidden}
.banner .hero{position:absolute;left:0;top:0;width:240px;height:168px;background:linear-gradient(135deg,#f4dcc0,#b8845a)}
.banner h2{position:absolute;right:14px;top:14px;color:#fff;font-weight:400;font-size:17px}
.banner .lead{position:absolute;right:14px;top:40px;width:250px;color:#fff;font-weight:700;font-size:12px;text-align:right;line-height:1.2}
.banner .cap{position:absolute;left:0;bottom:0;width:100%;height:36px;background:rgba(20,50,60,.85);color:#fff;font-size:12px;padding:10px 16px}

/* tabs */
.tabs{left:220px;top:423px;display:flex;gap:2px}
.tab{height:26px;padding:7px 14px;background:var(--tab);border:1px solid var(--line);border-bottom:0;font-weight:700;font-size:11px;width:158px}
.tab.on{background:var(--navy);color:#fff}
.products{left:210px;top:449px;width:562px;height:339px;display:grid;grid-template-columns:1fr 1fr;padding:0 12px}
.prod{display:flex;gap:14px;padding:12px 0 0 0;border-bottom:1px solid var(--line)}
.prod:nth-child(odd){border-right:1px solid var(--line)}
.prod:nth-child(even){padding-left:14px}
.prod:nth-child(n+3){border-bottom:0}
.prod .thumb{background:linear-gradient(135deg,#8fd0e0,#c96aa8);}
.prod.alt .thumb{background:linear-gradient(135deg,#d8a878,#6a3a2a)}
.prod h4{font-size:11px}
.prod p.d{font-size:10px;color:#444;line-height:1.35}
.links{margin:10px 0 18px;font-size:10px}
.links a{color:var(--red);text-decoration:underline}
.links a.g{color:var(--green)}
.was{font-size:10px;color:#888}
.was s{color:#888}
.today{color:var(--red);font-weight:700;font-size:11px}
.acts{display:flex;gap:6px;margin-top:8px;font-size:10px}
.acts span{padding:1px 6px;color:#fff}
.v{background:#333}.b{background:var(--orange)}

/* shop by category */
.shop-tab{left:220px;top:808px;width:164px;height:24px;background:var(--navy);color:#fff;font-weight:700;font-size:11px;padding:5px 13px}
.shop{left:210px;top:832px;width:562px;height:221px;display:grid;grid-template-columns:1fr 1fr;padding:10px 10px}
.scat{display:flex;gap:10px;height:100px}
.scat .thumb{width:94px;height:90px;background:linear-gradient(135deg,#e8ecf0,#9eb0c2)}
.scat.w .thumb{background:linear-gradient(135deg,#f0d6a8,#b8823a)}
.scat h4{font-size:11px}
.scat li{list-style:none;font-size:10px;color:#444;padding-top:7px;position:relative;padding-left:14px}
.scat li:before{content:"";position:absolute;left:2px;top:10px;width:6px;height:6px;border-radius:50%;border:2px solid var(--orange)}
.scat li.more{color:var(--orange-dark)}
.scat li.more:before{border:0;border-radius:0;width:8px;height:2px;top:13px;background:var(--orange)}

/* footer links */
.flinks{left:210px;top:1071px;width:562px;height:145px;display:grid;grid-template-columns:134px 134px 155px 1fr}
.flinks h5{font-size:11px;padding:10px 13px 12px;border-bottom:1px solid var(--line)}
.flinks ul{list-style:none;padding:8px 13px;border-right:1px solid var(--line);margin-right:-1px;height:100px}
.flinks div:last-child ul{border:0}
.flinks li{font-size:10px;padding:2px 0 2px 10px;position:relative}
.flinks li:before{content:"";position:absolute;left:0;top:6px;width:4px;height:4px;border:1px dotted #333}

/* right column */
.featured{left:784px;top:202px;width:184px;height:283px}
.fcat{margin:14px auto 0;width:150px;height:66px;border:1px solid var(--line);padding:2px;position:relative}
.fcat div{width:100%;height:100%}
.fcat span{position:absolute;right:2px;bottom:2px;background:rgba(0,0,0,.75);color:#fff;font-size:13px;padding:2px 8px}
.hot{left:784px;top:497px;width:184px;height:215px;background:#f4f4f4}
.hot .row{padding:12px 8px 10px 28px;border-bottom:1px solid #ddd;font-weight:600;font-size:12px;color:var(--navy);position:relative}
.hot .row:before{content:"";position:absolute;left:8px;top:13px;width:12px;height:12px;border-radius:50%;background:var(--orange)}
.hot .item{background:#fff;height:93px;position:relative;font-size:11px}
.shipping{left:784px;top:722px;width:184px;height:196px;padding:12px 12px 0 8px}
.ship{display:flex;justify-content:space-between;margin-bottom:12px;height:50px}
.ship .lbl{width:100px;border-bottom:2px solid var(--green);font-family:"Arimo",sans-serif;font-weight:700;color:var(--navy);font-size:20px;line-height:.9;padding-top:10px}
.ship .lbl small{display:block;font-size:11px}
.ship .tag{width:56px;height:50px;color:#fff;font-weight:700;text-align:center;font-size:12px;line-height:1;padding-top:10px;border-radius:2px}
.ship .tag b{font-size:16px;display:block}
</style>
</head>
<body>
<div class="stage">
  <div class="abs page"></div>

  <div class="abs brand"><span class="mark"></span>Steady Cart<small>.com.au</small></div>
  <div class="abs cart">My Shopping Cart <span class="ico"></span> | &nbsp;0 Items</div>
  <div class="abs follow"><span>Find us on<span class="sq"></span></span> | <span>Follow us on<span class="sq alt"></span></span></div>

  <nav class="abs nav">
    <div class="cats">ALL CATEGORIES <i></i></div>
    <ul style="margin-left:16px">
      <li>HOME</li><li>SPECIALS</li><li>HOT PRODUCTS</li><li>NEW PRODUCTS</li><li>ALL PRODUCTS</li><li><span class="live">LIVE</span> CHAT</li><li>LIVE HELP</li><li>CONTACTS</li>
    </ul>
  </nav>
  <div class="abs subnav">
    <a>My Account ▾</a><a>Help ▾</a><a>View Cart</a><a>Sign In</a><a>Register</a>
    <div class="search">Search <input type="text" aria-label="Search"> <span class="btn-go">Go</span></div>
  </div>

  <ul class="abs box cat-list">
    <li>Valentine’s Day Gifts</li><li>Cell Phones</li><li>Electronics</li><li>Video Games</li><li>Computer &amp; Networking</li><li>Health &amp; Beauty</li><li>Home &amp; Office</li><li>Toys &amp; Hobbies</li><li>Watches &amp; Jewelry</li><li>Sports &amp; Outdoors</li><li>Clothing &amp; Apparel</li><li>Gifts &amp; Party Supplies</li>
  </ul>

  <section class="abs box subscribe">
    <div class="side-head">Subscribe</div>
    <div class="row"><div class="field">your email here</div><span class="btn-go">Go</span></div>
    <div class="social">Find us on <span class="chip b">Friendbook</span></div>
    <div class="social">Follow us on <span class="chip t">Chirper</span></div>
  </section>

  <section class="abs box topdeal">
    <div class="side-head orange">Top Deal</div>
    <div class="deal"><div class="thumb" role="img" aria-label="Smartphone photo"></div><div><p>Nova 81 Slate Phone</p><p class="price">$389.00</p></div></div>
    <div class="deal" style="padding-top:20px"><div class="thumb" role="img" aria-label="Smartphone photo"></div><div><p>Nova 81 Slate Phone</p><p class="price">$389.00</p></div></div>
    <div class="deal" style="padding-top:20px"><div class="thumb" role="img" aria-label="Smartphone photo"></div><div><p>Nova 81 Slate Phone</p><p class="price">$389.00</p></div></div>
  </section>

  <section class="abs banner">
    <div class="hero" role="img" aria-label="Home stereo system with headphones and speakers"></div>
    <h2>BE AN ELECTRONIC JUNKIE</h2>
    <p class="lead">Lorem ipsum dolor sit amet consectetur adipiscing elit. Aliquam condimentum magna sit amet magna mattis venenatis. Donec sed erat a magna egestas placerat et ut lectus.</p>
    <div class="cap">Donec sed erat a magna egestas placerat et ut lectus.</div>
  </section>

  <div class="abs tabs">
    <div class="tab">Featured deal</div><div class="tab on">Special Promotion</div><div class="tab">Free Shipping</div>
  </div>
  <section class="abs box products">
    <article class="prod"><div class="thumb" role="img" aria-label="Folded colourful towels"></div><div><h4>Product Description</h4><p class="d">Lorem ipsum dolor sit amet consec<br>tetur adipiscing elit.</p><p class="links"><a>Add to Wishlist</a> &nbsp;| &nbsp;<a class="g">Add to Compare</a></p><p class="was">Dont pay: <s>$54.95</s></p><p class="today">Today’s Deal : $35.95</p><div class="acts"><span class="v">View</span><span class="b">Buy Now!</span></div></div></article>
    <article class="prod alt"><div class="thumb" role="img" aria-label="Perfume bottle in hand"></div><div><h4>Product Description</h4><p class="d">Lorem ipsum dolor sit amet consec<br>tetur adipiscing elit.</p><p class="links"><a>Add to Wishlist</a> &nbsp;| &nbsp;<a class="g">Add to Compare</a></p><p class="was">Dont pay: <s>$54.95</s></p><p class="today">Today’s Deal : $35.95</p><div class="acts"><span class="v">View</span><span class="b">Buy Now!</span></div></div></article>
    <article class="prod"><div class="thumb" role="img" aria-label="Folded colourful towels"></div><div><h4>Product Description</h4><p class="d">Lorem ipsum dolor sit amet consec<br>tetur adipiscing elit.</p><p class="links"><a>Add to Wishlist</a> &nbsp;| &nbsp;<a class="g">Add to Compare</a></p><p class="was">Dont pay: <s>$54.95</s></p><p class="today">Today’s Deal : $35.95</p><div class="acts"><span class="v">View</span><span class="b">Buy Now!</span></div></div></article>
    <article class="prod alt"><div class="thumb" role="img" aria-label="Perfume bottle in hand"></div><div><h4>Product Description</h4><p class="d">Lorem ipsum dolor sit amet consec<br>tetur adipiscing elit.</p><p class="links"><a>Add to Wishlist</a> &nbsp;| &nbsp;<a class="g">Add to Compare</a></p><p class="was">Dont pay: <s>$54.95</s></p><p class="today">Today’s Deal : $35.95</p><div class="acts"><span class="v">View</span><span class="b">Buy Now!</span></div></div></article>
  </section>

  <div class="abs shop-tab">Shop by Category</div>
  <section class="abs box shop">
    <div class="scat"><div class="thumb" role="img" aria-label="Health care photo"></div><ul><h4>Category Name</h4><li>Sub-Category name</li><li>Sub-Category name</li><li>Sub-Category name</li><li class="more">More Products</li></ul></div>
    <div class="scat" style="padding-left:32px"><div class="thumb" role="img" aria-label="Baby bouncer seat"></div><ul><h4>Category Name</h4><li>Sub-Category name</li><li>Sub-Category name</li><li>Sub-Category name</li><li class="more">More Products</li></ul></div>
    <div class="scat w" style="margin-top:8px"><div class="thumb" role="img" aria-label="Wooden pet kennel"></div><ul><h4>Category Name</h4><li>Sub-Category name</li><li>Sub-Category name</li><li>Sub-Category name</li><li class="more">More Products</li></ul></div>
    <div class="scat" style="padding-left:32px;margin-top:8px"><div class="thumb" role="img" aria-label="Diamond rings"></div><ul><h4>Category Name</h4><li>Sub-Category name</li><li>Sub-Category name</li><li>Sub-Category name</li><li class="more">More Products</li></ul></div>
  </section>

  <section class="abs box flinks">
    <div><h5>Join our community</h5><ul><li>Friendbook</li><li>Chirper</li><li>Our Blog</li></ul></div>
    <div><h5>Site utility</h5><ul><li>Faq</li><li>Site map</li><li>Discount Coupons</li></ul></div>
    <div><h5>Help Center</h5><ul><li>contact us</li><li>shipping &amp; Returns</li><li>Newsletter unsubscribe</li><li>Privacy Notice</li><li>Affiliate Help</li></ul></div>
    <div><h5>My Account</h5><ul><li>About Us</li><li>My Ordering Manager</li><li>Manage Address Book</li></ul></div>
  </section>

  <section class="abs box featured">
    <div class="side-head" style="font-size:14px">Featured Categories</div>
    <div class="fcat"><div role="img" aria-label="Small dog photo" style="background:linear-gradient(135deg,#d98a4a,#f3d2a6)"></div><span>Pet care</span></div>
    <div class="fcat"><div role="img" aria-label="Dining room furniture" style="background:linear-gradient(135deg,#8a3a1e,#e2c6a0)"></div><span>Furniture</span></div>
    <div class="fcat"><div role="img" aria-label="Gym equipment" style="background:linear-gradient(135deg,#c0661e,#4a4a4a)"></div><span>Gym</span></div>
  </section>

  <section class="abs box hot">
    <div class="row">Hottest Sale of this week</div>
    <div class="row">Best Deals in Cell Phones</div>
    <div class="row" style="border:0">Best Deals in Computers</div>
    <div class="item">
      <div class="abs" role="img" aria-label="Netbook computer" style="left:32px;top:2px;width:50px;height:44px;background:linear-gradient(#2a6ab0,#ddd)"></div>
      <div class="abs" style="left:104px;top:6px;color:#999"><s>USD 206.95</s></div>
      <div class="abs" style="left:104px;top:32px;color:var(--red);font-weight:700">USD 172.95</div>
      <div class="abs" style="left:12px;top:58px">Kestrel Netbook-400M Hz</div>
    </div>
  </section>

  <section class="abs box shipping">
    <div class="ship"><div class="lbl">FREE<small>SHIPPING</small></div><div class="tag" style="background:#139b45">Under<b>$25</b></div></div>
    <div class="ship"><div class="lbl" style="border-color:var(--orange)">FREE<small>SHIPPING</small></div><div class="tag" style="background:#f58a10">Under<b>$50</b></div></div>
    <div class="ship"><div class="lbl" style="border-color:#d01f3a">FREE<small>SHIPPING</small></div><div class="tag" style="background:#d01f3a">Under<b>$100</b></div></div>
  </section>

  <footer class="abs footer-bar">
    <span>© 2011 SteadyCart.com.au &nbsp;| &nbsp;All rights reserved &nbsp;| &nbsp;Terms of Use &nbsp;| &nbsp;Privacy Policy.</span>
    <span style="margin-left:auto;display:flex;gap:6px;align-items:center">
      <span style="width:60px;height:30px;border-radius:15px;border:2px solid #b0102a"></span>
      <span style="width:40px"></span>
      <span style="font-weight:700;color:var(--navy);font-size:12px">PayNest</span>
      <span style="width:22px;height:22px;border-radius:50%;background:#e8c84a"></span>
      <span style="width:24px;height:16px;background:#1a3a8a"></span>
      <span style="width:24px;height:16px;background:#c8201a"></span>
      <span style="width:24px;height:16px;background:#e07a10"></span>
      <span style="width:24px;height:16px;background:#2a6ab0"></span>
      <span style="width:24px;height:16px;background:#6a6a6a"></span>
      <span style="width:34px;height:16px;background:#ccc"></span>
    </span>
  </footer>
</div>
</body>
</html>
```